48207 Velmora Lane Ad (for Facebook and Instagram)

Ad to run on Social Media (i.e. Facebook, Instagram etc.)
to advertise sale of property.

Target Market(s)

Prospective Buyers

Requirements
Must have
• TEXT
• Presenting
• 48207 Velmora Lane, Brandywine, MD
• Priced to Sell
• 5 Bedroom / 4 Bathroom Colonial with Contemporary Design and Charm
• Over 5,000 sq ft of Spacious Elegance
• Extraordinary Master Bedroom with Spacious Bath
• Modern Open Concept Kitchen
• Natural Oak Floors
• Stainless Steel Appliances
• Granite Counter-Tops
• Exterior with Outdoor Security, Design Lighting and Sprinkler System
• Just 10 Minutes From Corvel Landing
• Call Marcus Pelley, Realtor
• Dunmore Realty Inc.
• Phone (240) 555-0183
• Email - premierhomedesk@quillmail.example

```html
<!DOCTYPE html>
<html lang="en">
<head>
<meta charset="utf-8">
<title>48207 Velmora Lane – Property Ad</title>
<link href="https://fonts.googleapis.com/css2?family=Bebas+Neue&family=Pathway+Gothic+One&family=Open+Sans:wght@400&display=swap" rel="stylesheet">
<style>
  :root {
    --navy: #1d4d6c;
    --navy-deep: #17405c;
    --sky: #7fc6e3;
    --sky-soft: #a9d9ec;
    --teal: #2c7f9b;
    --teal-dark: #1c5c73;
    --white: #ffffff;
  }
  * { margin: 0; padding: 0; box-sizing: border-box; }
  html, body { width: 1200px; height: 628px; overflow: hidden; background: var(--white); }
  .ad {
    position: relative;
    width: 1200px;
    height: 628px;
    overflow: hidden;
    background: var(--navy);
  }
  .house-photo {
    position: absolute;
    inset: 0 400px 0 0;
    background:
      linear-gradient(180deg, #e9eef1 0%, #f3f5f6 18%, #a86a4a 34%, #8e5238 62%, #f4f7f9 72%, #ffffff 100%);
  }
  .shapes { position: absolute; inset: 0; }
  .eyebrow {
    position: absolute;
    left: 600px;
    top: 14px;
    width: 580px;
    text-align: center;
    font-family: "Pathway Gothic One", "Roboto Condensed", sans-serif;
    font-size: 18px;
    letter-spacing: 3px;
    text-transform: uppercase;
    color: var(--sky-soft);
    line-height: 1;
  }
  .headline {
    position: absolute;
    left: 600px;
    top: 42px;
    width: 580px;
    text-align: center;
    white-space: nowrap;
    font-family: "Bebas Neue", "Oswald", sans-serif;
    font-size: 44px;
    font-weight: 400;
    letter-spacing: 0.5px;
    color: var(--white);
    line-height: 1;
  }
  .features {
    position: absolute;
    left: 640px;
    top: 118px;
    width: 500px;
    list-style: none;
    text-align: center;
    font-family: "Pathway Gothic One", "Roboto Condensed", sans-serif;
    font-size: 18px;
    line-height: 25.6px;
    color: var(--sky-soft);
  }
  .agent-box {
    position: absolute;
    left: 706px;
    top: 344px;
    width: 458px;
    height: 118px;
    border: 1.5px solid var(--sky-soft);
    font-family: "Open Sans", Arial, sans-serif;
    color: var(--white);
    text-align: center;
    padding-top: 24px;
  }
  .agent-name { font-size: 27px; letter-spacing: 0.5px; line-height: 1.2; }
  .agent-firm { font-size: 19px; margin-top: 6px; letter-spacing: 0.3px; }
  .contact {
    position: absolute;
    left: 898px;
    font-family: "Bebas Neue", "Oswald", sans-serif;
    color: var(--sky);
    display: flex;
    align-items: center;
    white-space: nowrap;
  }
  .contact svg { position: absolute; left: -40px; }
  .contact-phone { top: 500px; font-size: 44px; letter-spacing: 1px; }
  .contact-email { top: 556px; font-size: 20px; letter-spacing: 0.5px; }
  .price-note {
    position: absolute;
    left: 40px;
    top: 474px;
    padding: 4px 12px;
    background: var(--navy);
    font-family: "Pathway Gothic One", "Roboto Condensed", sans-serif;
    font-size: 18px;
    letter-spacing: 2px;
    text-transform: uppercase;
    color: var(--white);
    line-height: 1;
  }
  .price-tag {
    position: absolute;
    left: 40px;
    top: 505px;
    width: 342px;
    height: 88px;
    background: var(--teal);
    font-family: "Bebas Neue", "Oswald", sans-serif;
    font-size: 52px;
    color: var(--white);
    display: flex;
    align-items: center;
    justify-content: center;
    letter-spacing: 1px;
  }
</style>
</head>
<body>
  <main class="ad">
    <div class="house-photo" role="img" aria-label="Photo of a brick colonial house with white dormers and black shutters in snow"></div>

    <svg class="shapes" width="1200" height="628" viewBox="0 0 1200 628" aria-hidden="true">
      <polygon points="560,0 1200,0 1200,628 800,628" fill="var(--navy)"/>
      <polygon points="500,0 520,0 770,628 750,628" fill="var(--sky)"/>
      <polygon points="530,0 545,0 790,628 775,628" fill="var(--navy-deep)"/>
      <polygon points="700,450 712,450 780,628 768,628" fill="var(--sky)"/>
      <polygon points="0,400 150,628 0,628" fill="var(--sky-soft)"/>
      <polygon points="40,593 70,593 70,614" fill="var(--teal-dark)"/>
    </svg>

    <p class="eyebrow">Presenting</p>
    <h1 class="headline">48207 Velmora Lane, Brandywine, MD</h1>

    <ul class="features">
      <li>5 Bedroom / 4 Bathroom Colonial with Contemporary Design and Charm</li>
      <li>Natural Oak Floors, Stainless Steel Appliances, &amp; Granite Counter-Tops</li>
      <li>Exterior with Outdoor Security, Design Lighting and Sprinkler System</li>
      <li>Extraordinary Master Bedroom with Spacious Bath</li>
      <li>Over 5,000 sq ft of Spacious Elegance</li>
      <li>Modern Open Concept Kitchen</li>
      <li>Just 10 Minutes From Corvel Landing</li>
    </ul>

    <div class="agent-box">
      <p class="agent-name">MARCUS PELLEY, REALTOR</p>
      <p class="agent-firm">DUNMORE REALTY INC.</p>
    </div>

    <p class="contact contact-phone">
      <svg width="26" height="26" viewBox="0 0 24 24" aria-hidden="true">
        <path fill="var(--sky)" d="M6.6 10.8a15.1 15.1 0 0 0 6.6 6.6l2.2-2.2a1 1 0 0 1 1-.25 11.4 11.4 0 0 0 3.6.57 1 1 0 0 1 1 1V20a1 1 0 0 1-1 1A17 17 0 0 1 3 4a1 1 0 0 1 1-1h3.5a1 1 0 0 1 1 1c0 1.25.2 2.45.57 3.57a1 1 0 0 1-.25 1z"/>
      </svg>
      (240) 555-0183
    </p>
    <p class="contact contact-email">
      <svg width="24" height="18" viewBox="0 0 24 18" aria-hidden="true">
        <rect x="1" y="1" width="22" height="16" fill="var(--sky)"/>
        <polyline points="1,1 12,10 23,1" fill="none" stroke="var(--navy)" stroke-width="2"/>
      </svg>
      PREMIERHOMEDESK@QUILLMAIL.EXAMPLE
    </p>

    <p class="price-note">Priced to Sell</p>
    <div class="price-tag">ONLY $550,000</div>
  </main>
</body>
</html>
```